Business Card Design Project

Business card for law firm
Use existing logo
Must have:
Gerald P. Whitcombe
2715-C West 6th
McAllen, TX 78521
gwhitcombe@dvlegalgroup.com
www.dvlegalgroup.com
956-412-3095

Target Market(s)

Clients and potential clients, generally adult, business background

Industry/Entity Type

Business

Requirements
Must have
• Our logo, see below

```html
<!DOCTYPE html>
<html lang="en">
<head>
<meta charset="utf-8">
<title>Dalton Vance – Business Card</title>
<link rel="stylesheet" href="https://fonts.googleapis.com/css2?family=EB+Garamond:wght@400;500&display=swap">
<style>
  :root {
    --page: #ffffff;
    --panel: #0d0d0d;
    --block: #737373;
    --ink-light: #ffffff;
    --ink-muted: #6e6e6e;
  }
  html, body {
    margin: 0;
    padding: 0;
    width: 1200px;
    height: 900px;
    overflow: hidden;
    background: var(--page);
  }
  .canvas {
    position: relative;
    width: 1200px;
    height: 900px;
    font-family: "EB Garamond", Garamond, serif;
  }
  .card-art {
    position: absolute;
    left: 0;
    top: 0;
  }
  .firm {
    position: absolute;
    left: 463px;
    top: 155px;
    width: 642px;
    display: flex;
    align-items: flex-start;
    gap: 12px;
  }
  .firm-square {
    width: 78px;
    height: 78px;
    background: var(--ink-light);
    flex: none;
  }
  .firm-text {
    flex: 1;
    color: var(--ink-light);
  }
  .firm-name {
    margin: -4px 0 0;
    font-size: 50px;
    font-weight: 400;
    font-variant: small-caps;
    letter-spacing: 1px;
    line-height: 54px;
    border-bottom: 1.5px solid var(--ink-light);
  }
  .firm-tagline {
    margin: 2px 0 0;
    font-size: 23px;
    font-variant: small-caps;
    letter-spacing: 0.5px;
    line-height: 26px;
  }
  .person {
    position: absolute;
    right: 105px;
    top: 418px;
    margin: 0;
    font-size: 44px;
    font-weight: 400;
    color: var(--ink-light);
    line-height: 52px;
  }
  .contact {
    position: absolute;
    right: 95px;
    top: 523px;
    margin: 0;
    font-style: normal;
    font-size: 30px;
    line-height: 40px;
    text-align: right;
    color: var(--ink-muted);
  }
</style>
</head>
<body>
<main class="canvas">
  <svg class="card-art" width="1200" height="900" viewBox="0 0 1200 900" aria-hidden="true">
    <rect class="side-block" x="47" y="135" width="360" height="603" fill="var(--block)"/>
    <rect class="info-panel" x="437" y="135" width="696" height="603" fill="var(--panel)"/>
  </svg>

  <header class="firm">
    <div class="firm-square"></div>
    <div class="firm-text">
      <h1 class="firm-name">Dalton Vance</h1>
      <p class="firm-tagline">Attorneys and Councelors</p>
    </div>
  </header>

  <h2 class="person">Gerald P. Whitcombe</h2>

  <address class="contact">
    2715-C West 6th<br>
    McAllen, TX 78521<br>
    gwhitcombe@dvlegalgroup.com<br>
    www.dvlegalgroup.com<br>
    956-412-3095
  </address>
</main>
</body>
</html>
```